ZB - WESITE NEEDED PAGE: Clean / Modern / Pro & Dynamic

Zephyl-Brokers is a new insurance brokerage firm dealing exclusively with companies (BToB) providing the following property: Liabilities Insurance Insurances Automobile Insurance Insurances Construction% 26amp; Engineering Casualty Workmen 's Compensation Health Insurance Marime% 26amp; Transit Credit Insurance Young, Fast, Proactive and Dynamic we call ourselves Zephyl-Brokers because we are a "start-up" willing to make a difference in the market, bringing modernity and speed to our industry, still too bureaucratic / procedural / opaque uninitiated. We need something respecting the colors of our orange logtype; blue; white; black; easy to scroll, with simple information on the company; - who we are - our team (with the pictures) - what we do - what we do - contact us, contact us (google map) Luanda (Angola) Small company, just need something flashy / professional / structured / modern.

Target Market(s)

BtoB; Oil and gas companies; French speaking copying established in Angola, all industrials, factories and importers of goods.

Industry/Entity Type

Insurance Broker

Font styles to use
Sans Serif

Colors

Requirements
Must have
• We need something respecting the colors of our orange logtype; blue; white; black; easy to scroll, with simple information on the company; - who we are - our team (with the pictures) - what we do - what we do - contact us, contact us (google map) Luanda (Angola) Small company, just need something flashy / professional / structured / modern.
Nice to have
• A page format
Should not have
• WE DO NOT WANT A REFER TO OUR LOGO, but a Home Page for our Website with the basics categories ... >> PLEASE CAREFULLY USE THE RIGHT COLOR OF THE LOGOTYPE which are the ones enclosed Orange / Turquoise / Black as per the business card .

```html
<!DOCTYPE html>
<html lang="en">
<head>
<meta charset="utf-8">
<title>Zephyl-Brokers – Home Page</title>
<link rel="stylesheet" href="https://fonts.googleapis.com/css2?family=Comfortaa:wght@400;600;700&family=Montserrat:wght@300;400;600;700&family=Quicksand:wght@400&display=swap">
<style>
:root{
  --orange:#f46523;
  --black:#151515;
  --blue:#25aae1;
  --cream:#f8f5e4;
  --white:#ffffff;
  --board:#f7f7f7;
  --text:#3a3a3a;
  --muted:#777;
  --display:'Comfortaa', sans-serif;
  --sans:'Montserrat', sans-serif;
}
*{box-sizing:border-box;margin:0;padding:0}
html,body{width:1200px;height:3829px;overflow:hidden}
body{background:var(--board);font-family:var(--sans);color:var(--text);position:relative}
.abs{position:absolute}
.brand-name{font-family:var(--sans);font-weight:600;color:var(--black);letter-spacing:0}
.brand-mark{display:inline-block;width:10px;height:10px;background:var(--blue)}

/* style guide */
.brand-top{left:0;width:1200px;top:56px;display:flex;align-items:center;justify-content:center;gap:8px}
.brand-top .brand-name{font-size:16px}
.guide-label{font-family:var(--sans);font-size:26px;letter-spacing:9px;color:var(--black);font-weight:400}
.font-line{left:62px;top:215px;width:0;height:170px;border-left:1px dashed #9cc9e0}
.font-item{left:84px;color:#444;white-space:nowrap}
.font-item::before{content:"";position:absolute;left:-25px;top:50%;width:7px;height:7px;border-radius:50%;background:var(--blue);transform:translateY(-50%)}
.swatch{width:133px;height:42px;font-size:10px;font-weight:700;display:flex;align-items:center;justify-content:center;color:#fff}
.page-label{left:0;width:1200px;top:456px;text-align:center;font-size:22px;letter-spacing:16px;color:#555}

/* page frame */
.page{left:61px;top:537px;width:1078px;height:3237px;background:var(--cream);box-shadow:0 4px 30px rgba(0,0,0,.08)}
.hero{left:205px;top:537px;width:934px;height:496px;background:linear-gradient(135deg,#f46523,#f0741f);box-shadow:0 12px 30px rgba(244,101,35,.25)}
.logo-tab{left:245px;top:537px;width:174px;height:88px;background:var(--white);display:flex;align-items:center;justify-content:center;gap:7px}
.logo-tab .brand-name{font-size:14px}
.nav{left:477px;top:567px;display:flex;gap:25px;font-size:10px;font-weight:600;color:#fff;text-transform:uppercase;white-space:nowrap}
.btn{border-radius:30px;font-family:var(--sans);font-weight:600;text-transform:uppercase;display:flex;align-items:center;justify-content:center;font-size:10px;white-space:nowrap}
.btn-blue{background:var(--blue);color:#fff}
.btn-outline{border:2px solid var(--blue);color:var(--black);background:#fff}
.hero-welcome{left:277px;top:678px;font-family:var(--display);font-size:20px;color:var(--black)}
.hero-title{left:277px;top:712px;font-family:var(--display);font-weight:600;font-size:47px;line-height:50px;color:#fff;white-space:nowrap}
.hero-sub{left:277px;top:834px;font-size:13.5px;font-weight:700;color:#fff}
.art{border-radius:2px}

.section-title{font-family:var(--display);font-weight:600;font-size:40px;color:var(--black);text-align:center;left:61px;width:1078px}
.white-band{left:61px;background:var(--white);width:1078px}

.service{top:1260px;width:240px;text-align:center}
.service h3{font-size:13px;font-weight:700;color:var(--black);margin:22px 0 14px}
.service p{font-size:11px;color:var(--muted);line-height:16px}
.service svg{display:block;margin:0 auto}
.service-card{left:465px;top:1231px;width:268px;height:199px;background:#fff;box-shadow:0 4px 20px rgba(0,0,0,.08)}

.who{left:205px;top:1932px;width:788px;height:243px;background:#fff;padding:40px 47px}
.who h2{font-family:var(--display);font-weight:600;font-size:36px;color:var(--black);margin-bottom:24px}
.who p{font-size:11px;line-height:16px;color:#555;margin-bottom:14px}

.avatar{border-radius:50%;border:4px solid #fff;background:linear-gradient(135deg,#c9a48a,#6b5146);box-shadow:0 3px 10px rgba(0,0,0,.2)}
.team-card{left:470px;top:2370px;width:210px;height:119px;background:var(--orange);color:#fff;padding:18px 22px}
.team-card h4{font-size:13px;font-weight:600;margin-bottom:6px}
.team-card p{font-size:10px;line-height:13px;margin-bottom:10px}
.team-card .btn{border:1.5px solid #fff;width:80px;height:23px;font-size:8px;text-transform:none;color:#fff}

.testimonial{top:2773px;background:var(--cream);text-align:center;padding:20px 18px}
.testimonial.active{background:#fff;box-shadow:0 4px 20px rgba(0,0,0,.08)}
.testimonial h4{font-size:13px;font-weight:700;color:var(--black);margin-bottom:10px}
.testimonial p{font-size:11px;font-style:italic;color:#777;line-height:17px}
.quote{font-family:Georgia,serif;font-size:48px;font-weight:700;line-height:40px;width:100%;text-align:center}

.cta{left:61px;top:3308px;width:1078px;height:111px;background:linear-gradient(90deg,#f46523,#f79a24 60%,#fcd333)}
.cta h2{position:absolute;left:144px;top:22px;font-family:var(--display);font-weight:600;font-size:38px;color:var(--black)}
.cta p{position:absolute;left:144px;top:70px;font-size:11.5px;font-weight:600;color:var(--black)}

.footer{left:61px;top:3494px;width:934px;height:280px;background:var(--black);color:#ddd}
.footer-title{font-family:var(--display);font-weight:600;font-size:20px;color:#fff}
</style>
</head>
<body>

<!-- brand + style guide -->
<div class="abs brand-top"><span class="brand-mark"></span><span class="brand-name">Zephyl-Brokers</span></div>

<div class="abs guide-label" style="left:57px;top:135px">FONT</div>
<div class="abs font-line"></div>
<div class="abs font-item" style="top:195px;font-family:var(--display);font-weight:600;font-size:40px;letter-spacing:2px">Resagnicto - Bold</div>
<div class="abs font-item" style="top:262px;font-family:var(--sans);font-weight:700;font-size:27px">Montserrat - Bold</div>
<div class="abs font-item" style="top:320px;font-family:var(--sans);font-weight:400;font-size:20px">Montserrat - Light, Regular</div>
<div class="abs font-item" style="top:373px;font-family:'Quicksand',sans-serif;font-size:18px">Sanseriffic - Regular</div>

<div class="abs guide-label" style="left:852px;top:135px">COLOR</div>
<div class="abs swatch" style="left:852px;top:192px;background:var(--orange)">#f46523</div>
<div class="abs swatch" style="left:1005px;top:192px;background:var(--black)">#151515</div>
<div class="abs swatch" style="left:852px;top:247px;background:var(--blue)">#25aae1</div>
<div class="abs swatch" style="left:1005px;top:247px;background:var(--cream);color:var(--black);box-shadow:0 2px 6px rgba(0,0,0,.1)">#f8f5e4</div>

<div class="abs page-label">HOME PAGE</div>

<!-- page -->
<div class="abs page"></div>

<!-- hero -->
<div class="abs hero"></div>
<div class="abs logo-tab"><span class="brand-mark"></span><span class="brand-name">Zephyl-Brokers</span></div>
<nav class="abs nav"><span>Home</span><span>About Us</span><span>Who We Are</span><span>Our Team</span><span>What We Do</span><span>Contact Us</span></nav>
<div class="abs btn btn-blue" style="left:1017px;top:561px;width:95px;height:28px;font-size:9px">Get Started</div>
<svg class="abs" style="left:205px;top:537px" width="934" height="496" viewBox="0 0 934 496">
  <line x1="888" y1="85" x2="888" y2="460" stroke="#151515" stroke-width="2"/>
  <circle cx="888" cy="85" r="3" fill="#151515"/>
  <path d="M77 458 L83 466 L888 466" fill="none" stroke="#151515" stroke-width="2"/>
  <circle cx="77" cy="457" r="3" fill="#151515"/>
</svg>
<div class="abs hero-welcome">Welcome to Zephyl Brokers</div>
<div class="abs hero-title">Be Life Confident<br>With Zephyl Broker</div>
<div class="abs hero-sub">We Are One Of The Most Effective Insurance Company</div>
<div class="abs btn btn-blue" style="left:277px;top:883px;width:136px;height:48px">Contact Us</div>
<div class="abs art" role="img" aria-label="Illustration of a hand holding a city with a car, house, clock, coins and briefcase" style="left:756px;top:680px;width:383px;height:300px;background:radial-gradient(ellipse at 45% 55%,#3b3f66 0%,#c74a2a 55%,rgba(244,101,35,0) 72%)"></div>

<!-- what we do -->
<div class="abs section-title" style="top:1078px">What We Do</div>
<div class="abs white-band" style="top:1170px;height:585px"></div>
<svg class="abs" style="left:589px;top:1170px" width="20" height="12"><polygon points="0,0 20,0 10,10" fill="var(--cream)"/></svg>

<div class="abs service-card"></div>
<div class="abs service" style="left:215px">
  <svg width="50" height="48" viewBox="0 0 50 48" fill="none" stroke="var(--blue)" stroke-width="2"><rect x="4" y="16" width="14" height="30"/><rect x="18" y="4" width="14" height="42"/><rect x="32" y="20" width="14" height="26"/><path d="M8 22h6M8 30h6M22 12h6M22 20h6M22 28h6M36 28h6M36 36h6"/></svg>
  <h3>Liabilities Insurance</h3><p>t enim ad minim veniam, quis<br>nostrud exercitation ullamco</p>
</div>
<div class="abs service" style="left:479px">
  <svg width="60" height="48" viewBox="0 0 60 48"><path d="M12 20 L18 6 H42 L48 20 H54 V40 H46 V46 H38 V40 H22 V46 H14 V40 H6 V20 Z" fill="var(--orange)"/><rect x="20" y="10" width="20" height="9" fill="#fff"/><circle cx="15" cy="29" r="4" fill="#fff"/><circle cx="45" cy="29" r="4" fill="#fff"/><rect x="24" y="27" width="12" height="4" fill="#fff"/></svg>
  <h3>Automobile Insurance</h3><p>t enim ad minim veniam, quis<br>nostrud exercitation ullamco</p>
</div>
<div class="abs service" style="left:744px">
  <svg width="54" height="48" viewBox="0 0 54 48" fill="none" stroke="var(--blue)" stroke-width="2"><rect x="4" y="18" width="14" height="28"/><rect x="18" y="10" width="14" height="36"/><path d="M36 46V8l14 6M36 8h14v8M50 16v10"/><path d="M8 24h6M8 32h6M22 18h6M22 26h6M22 34h6"/></svg>
  <h3>Construction Insurance</h3><p>t enim ad minim veniam, quis<br>nostrud exercitation ullamco</p>
</div>
<div class="abs" style="left:205px;top:1427px;width:788px;height:2px;background:#ece7c9"></div>
<div class="abs btn btn-outline" style="left:520px;top:1484px;width:155px;height:46px">View All Services</div>

<div class="abs" style="left:61px;top:1755px;width:1078px;height:847px;background:var(--cream)"></div>
<div class="abs art" role="img" aria-label="Illustration of hands holding an umbrella, family, house, car, coins, heart, globe and an insurance policy" style="left:205px;top:1591px;width:788px;height:294px;background:linear-gradient(180deg,rgba(255,255,255,0) 0%,rgba(255,255,255,0) 30%,#dbe9f2 30%,#c9dbe8 100%)"></div>
<svg class="abs" style="left:270px;top:1922px" width="20" height="12"><polygon points="0,12 20,12 10,2" fill="#fff"/></svg>

<!-- who we are -->
<div class="abs who">
  <h2>Who Zephyl Brokers Are</h2>
  <p>Lorem ipsum dolor sit amet, consectetur adipiscing elit, sed do eiusmod tempor incididunt ut labore et dolore magna aliqua. Ut enim ad minim veniam, quis nostrud exercitation ullamco laboris nisi ut aliquip ex ea commodo consequat.</p>
  <p>Duis aute irure dolor in reprehenderit in voluptate velit esse cillum dolore eu fugiat nulla pariatur. Excepteur sint occaecat cupidatat non proident, sunt in culpa qui officia deserunt mollit anim id est laborum.Lorem ipsum dolor sit amet, consectetur adipiscing elit, sed do eiusmod tempor incididunt ut labore et dolore magna aliqua.</p>
</div>

<!-- team -->
<div class="abs section-title" style="top:2226px">Our Team</div>
<div class="abs art" role="img" aria-label="Faint world map behind the team members" style="left:268px;top:2283px;width:684px;height:289px;background:radial-gradient(ellipse at 50% 45%,#e5dfc7 0%,rgba(229,223,199,.4) 55%,rgba(248,245,228,0) 75%)"></div>
<div class="abs avatar" role="img" aria-label="Team member photo" style="left:250px;top:2320px;width:38px;height:38px"></div>
<div class="abs avatar" role="img" aria-label="Team member photo" style="left:343px;top:2301px;width:38px;height:38px"></div>
<div class="abs avatar" role="img" aria-label="Team member photo" style="left:513px;top:2344px;width:38px;height:38px"></div>
<div class="abs avatar" role="img" aria-label="Team member photo" style="left:770px;top:2286px;width:78px;height:78px"></div>
<div class="abs avatar" role="img" aria-label="Team member photo" style="left:684px;top:2382px;width:38px;height:38px"></div>
<div class="abs avatar" role="img" aria-label="Team member photo" style="left:812px;top:2446px;width:38px;height:38px"></div>
<div class="abs avatar" role="img" aria-label="Team member photo, Lucinda" style="left:384px;top:2407px;width:72px;height:72px;border-color:var(--orange)"></div>
<div class="abs team-card"><h4>Lucinda</h4><p>t enim ad minim veniam, quis<br>nostrud exercitation ullamco</p><div class="btn">Learn More</div></div>

<!-- testimonials -->
<div class="abs white-band" style="top:2602px;height:446px"></div>
<div class="abs section-title" style="top:2664px">What Our Client Says</div>
<div class="abs quote" style="left:205px;width:238px;top:2752px;color:#e6dfbd">&ldquo;</div>
<div class="abs quote" style="left:465px;width:268px;top:2752px;color:var(--orange)">&ldquo;</div>
<div class="abs quote" style="left:754px;width:239px;top:2752px;color:#e6dfbd">&ldquo;</div>
<div class="abs testimonial" style="left:205px;width:238px;height:141px"><h4>John Smith</h4><p>Lorem ipsum dolor sit amet, consectetur adipiscing elit, sed do eiusmod tempor incididunt ut labore et dolore magna aliqua. Ut enim ad minim</p></div>
<div class="abs testimonial active" style="left:465px;width:268px;height:190px"><h4>Lucinda</h4><p>Lorem ipsum dolor sit amet, consectetur adipiscing elit, sed do eiusmod tempor incididunt ut labore et dolore magna aliqua. Ut enim ad minim veniam, quis nostrud exercitation ullamco laboris nisi<br><br>ut aliquip ex ea commodo consequat.</p></div>
<div class="abs testimonial" style="left:754px;width:239px;height:141px"><h4>Merry Deo</h4><p>Lorem ipsum dolor sit amet, consectetur adipiscing elit, sed do eiusmod tempor incididunt ut labore et dolore magna aliqua. Ut enim ad minim veniam.</p></div>

<!-- map -->
<div class="abs art" role="img" aria-label="Street map showing the office location" style="left:61px;top:3048px;width:1078px;height:260px;background:linear-gradient(180deg,#ebebeb,#dcdcdc)"></div>
<svg class="abs" style="left:486px;top:3123px" width="14" height="18" viewBox="0 0 14 18"><path d="M7 1a6 6 0 0 0-6 6c0 4.5 6 10 6 10s6-5.5 6-10a6 6 0 0 0-6-6z" fill="none" stroke="#333" stroke-width="1.6"/><circle cx="7" cy="7" r="2" fill="#333"/></svg>
<div class="abs" style="left:504px;top:3127px;font-size:10px;font-weight:600;color:#333">Shop Name</div>
<div class="abs" style="left:510px;top:3168px;width:244px;height:52px;background:#fff;box-shadow:0 2px 8px rgba(0,0,0,.12);font-size:9px;color:#555;padding:10px 10px 0 30px;line-height:13px">Lorem Ipsum Dolor Sit Amet Conse ctetor Dolor Sit Amet Lorem Ipsum Dolor.</div>
<svg class="abs" style="left:522px;top:3178px" width="12" height="16" viewBox="0 0 12 16"><path d="M6 1a5 5 0 0 0-5 5c0 4 5 9 5 9s5-5 5-9a5 5 0 0 0-5-5z" fill="var(--orange)"/><circle cx="6" cy="6" r="2" fill="#fff"/></svg>
<div class="abs" style="left:1070px;top:3058px;width:62px;height:18px;background:#fff;font-size:8px;display:flex;gap:8px;align-items:center;justify-content:center;box-shadow:0 1px 3px rgba(0,0,0,.2)"><b>Map</b><span>Satellite</span></div>
<svg class="abs" style="left:70px;top:3060px" width="36" height="150"><circle cx="18" cy="16" r="14" fill="#fff" stroke="#aaa"/><path d="M18 7v5M18 20v5M9 16h5M22 16h5" stroke="#666" stroke-width="1.5"/><rect x="13" y="48" width="10" height="18" rx="3" fill="#f3a623"/><line x1="18" y1="80" x2="18" y2="145" stroke="#aaa"/><rect x="14" y="74" width="8" height="8" fill="#fff" stroke="#aaa"/></svg>

<!-- CTA -->
<div class="abs cta"><h2>Lets Get Started</h2><p>Consectetur adipiscing elit, sed do eiusmod tempor incididunt ut labore et dolore magna aliqua.</p></div>
<div class="abs btn btn-blue" style="left:850px;top:3343px;width:143px;height:40px">Contact Us</div>

<!-- footer -->
<div class="abs footer"></div>
<div class="abs footer-title" style="left:205px;top:3541px">Contact Us</div>
<svg class="abs" style="left:205px;top:3585px" width="12" height="16" viewBox="0 0 12 16"><path d="M6 1a5 5 0 0 0-5 5c0 4 5 9 5 9s5-5 5-9a5 5 0 0 0-5-5z" fill="none" stroke="#ddd" stroke-width="1.5"/><circle cx="6" cy="6" r="1.8" fill="#ddd"/></svg>
<div class="abs" style="left:227px;top:3585px;font-size:10.5px;line-height:12px;color:#ddd">Lorem Ipsum Dolor Sit<br>Amet Consectetor</div>
<svg class="abs" style="left:205px;top:3630px" width="13" height="13" viewBox="0 0 24 24"><path d="M6.6 10.8a15 15 0 0 0 6.6 6.6l2.2-2.2a1 1 0 0 1 1-.25 11.4 11.4 0 0 0 3.6.57 1 1 0 0 1 1 1V20a1 1 0 0 1-1 1A17 17 0 0 1 3 4a1 1 0 0 1 1-1h3.5a1 1 0 0 1 1 1c0 1.25.2 2.45.57 3.57a1 1 0 0 1-.25 1z" fill="#ddd"/></svg>
<div class="abs" style="left:227px;top:3631px;font-size:10.5px;color:#ddd">1300 555 010</div>
<svg class="abs" style="left:205px;top:3664px" width="14" height="11" viewBox="0 0 14 11"><rect x="1" y="1" width="12" height="9" fill="none" stroke="var(--orange)" stroke-width="1.3"/><path d="M1 1l6 5 6-5" fill="none" stroke="var(--orange)" stroke-width="1.3"/></svg>
<div class="abs" style="left:227px;top:3662px;font-size:10.5px;color:var(--orange)">info@zephylbrokers.com</div>
<div class="abs" style="left:205px;top:3726px;font-size:9.5px;color:#bbb">© 2019 Zephyl Brokers. All Rights Reserved.</div>

<div class="abs footer-title" style="left:456px;top:3541px">Navigation</div>
<div class="abs" style="left:456px;top:3580px;font-size:10.5px;line-height:21.5px;color:#ccc">
  <div style="color:var(--orange)">Home</div><div>Who We Are</div><div>What We Do</div><div>About Us</div><div>Our Team</div><div>Contact Us</div>
</div>

<div class="abs footer-title" style="left:647px;top:3541px;line-height:23px;white-space:nowrap">Integrated Innovations –<br>We are here to help you!</div>
<div class="abs" style="left:647px;top:3603px;font-size:10.5px;color:#ccc">A Better Tomorrow, Through Intelligent use of Technology</div>
<div class="abs btn btn-blue" style="left:647px;top:3639px;width:154px;height:34px;font-size:9px">Contact Us Now!</div>

</body>
</html>
```